Business Card Design

5* Hotel Property based on an island in Greece

My position is aparta from being a director, i'm on the accounts payable too, not sure how this should be stated, with a comma or "/"?

Sorry about the uploaded logo, it was a mistaken one!

There's also need to be added this  www.corvanteholdings.com on the back side of the card!

Also need to have the logo of the corvante holdings which can be found in a second on the brief! Thank you guys, irini

Industry/Entity Type

Business

Contact Information for Business Card

VERISTOKA PELLA Hotel
Irini Dravetsou
Director, AP Dept.

www.veristoka.gr
Peltira Island 85300
Greece

irinidravetsou@fenmail.com
+306951273064

```html
<!DOCTYPE html>
<html lang="en">
<head>
<meta charset="utf-8">
<title>Veristoka Pella Hotel – Business Card</title>
<link rel="stylesheet" href="https://fonts.googleapis.com/css2?family=Tinos&family=Arimo&display=swap">
<style>
  :root {
    --backdrop: #b52222;
    --card-lilac: #8e8eee;
    --card-silver-light: #f6f6f6;
    --card-silver-dark: #b9b9b9;
    --card-edge: #1c1c1c;
    --ink-dark: #2b2b2b;
    --ink-black: #141414;
    --ink-white: #ffffff;
    --title-orange: #e07c3c;
    --mark-blue: #3aaee0;
    --serif: "Tinos", "Times New Roman", serif;
    --sans: "Arimo", Arial, sans-serif;
  }
  * { margin: 0; padding: 0; box-sizing: border-box; }
  html, body { width: 1137px; height: 1200px; overflow: hidden; background: var(--backdrop); }
  .canvas { position: relative; width: 1137px; height: 1200px; background: var(--backdrop); }

  .card-back { position: absolute; left: 56px; top: 33px; width: 948px; height: 626px; }
  .card-back svg { display: block; }

  .brand-back { position: absolute; left: 356px; top: 366px; font-family: var(--sans); color: var(--ink-dark); }
  .brand-back .brand-name { font-size: 56px; line-height: 1; letter-spacing: -0.5px; }
  .brand-back .brand-type { font-size: 33px; line-height: 1; letter-spacing: 10px; margin-top: 10px; }

  .card-front {
    position: absolute; left: 128px; top: 544px; width: 950px; height: 626px;
    background: var(--card-lilac); border-radius: 40px;
  }
  .mark { position: absolute; border-radius: 50%; background: var(--mark-blue); }
  .brand-front { position: absolute; left: 557px; top: 45px; font-family: var(--sans); color: var(--ink-white); }
  .brand-front .brand-name { font-size: 31px; line-height: 1; }
  .brand-front .brand-type { font-size: 20px; line-height: 1; letter-spacing: 6px; margin-top: 6px; }

  .holder-name { position: absolute; left: 39px; top: 160px; font-family: var(--serif); font-size: 67px; line-height: 1; color: var(--ink-white); }
  .holder-title { position: absolute; left: 39px; top: 235px; font-family: var(--serif); font-size: 44px; line-height: 1; color: var(--title-orange); }

  .detail { position: absolute; font-family: var(--serif); text-align: center; }
  .detail .label { font-size: 39px; line-height: 1; color: var(--ink-black); }
  .detail .value { font-size: 40px; line-height: 1.25; color: var(--ink-white); }
  .detail-address { left: 37px; top: 330px; width: 340px; }
  .detail-address .value { text-align: left; margin-top: 4px; }
  .detail-web { left: 415px; top: 329px; width: 500px; }
  .detail-web .value { margin-top: 2px; }
  .detail-phone { left: 57px; top: 492px; width: 300px; }
  .detail-email { left: 395px; top: 490px; width: 540px; }
  .detail-email .value { font-size: 39px; }
</style>
</head>
<body>
<main class="canvas">
  <section class="card-back" aria-label="Card back">
    <svg width="948" height="626" viewBox="0 0 948 626" aria-hidden="true">
      <defs>
        <radialGradient id="silver" cx="0.5" cy="0.55" r="0.7">
          <stop offset="0" stop-color="var(--card-silver-light)"/>
          <stop offset="1" stop-color="var(--card-silver-dark)"/>
        </radialGradient>
        <clipPath id="backShape"><rect x="0" y="0" width="948" height="626" rx="37"/></clipPath>
      </defs>
      <g clip-path="url(#backShape)">
        <rect width="948" height="626" fill="url(#silver)"/>
        <path d="M0 0 H948 V312 Q474 400 0 312 Z" fill="var(--card-lilac)"/>
      </g>
      <rect x="1" y="1" width="946" height="624" rx="37" fill="none" stroke="var(--card-edge)" stroke-width="2"/>
    </svg>
    <div class="mark" style="left:79px;top:282px;width:192px;height:192px;"></div>
    <div class="brand-back" style="left:300px;top:333px;">
      <div class="brand-name">VERISTOKA PELLA</div>
      <div class="brand-type">HOTEL</div>
    </div>
  </section>

  <section class="card-front" aria-label="Card front">
    <div class="mark" style="left:427px;top:20px;width:112px;height:112px;"></div>
    <div class="brand-front">
      <div class="brand-name">VERISTOKA PELLA</div>
      <div class="brand-type">HOTEL</div>
    </div>

    <div class="holder-name">Irini Dravetsou</div>
    <div class="holder-title">Director, AP Dept.</div>

    <div class="detail detail-address">
      <div class="label">Postal Address</div>
      <div class="value">Peltira Island,<br>85300 Greece</div>
    </div>
    <div class="detail detail-web">
      <div class="label">Website</div>
      <div class="value">www.veristoka.gr</div>
    </div>
    <div class="detail detail-phone">
      <div class="label">Contact Info</div>
      <div class="value">+306951273064</div>
    </div>
    <div class="detail detail-email">
      <div class="label">Email</div>
      <div class="value">irinidravetsou@fenmail.com</div>
    </div>
  </section>
</main>
</body>
</html>
```